Talvoro Web Design

We need a redesign of our current website www.talvoro-example.com

THIS IS A DESIGN STAGE ONLY

We have attached details of the whole project for your understanding only

We do not want to change our Logo but do want to have a more modern and intuitive feel to the site.

The first stage is the design but we are also looking for a coder to take the site to the next level

Talvoro has a current website that has been in operation for the past 6 years the design was based around the Saas self-service model and while functional does not meet Talvoro needs with regard to the new positioning.

We are happy to stay in Fendrix or will look at alternatives

The purpose of the redesign is to align the look and feel of the website to meet our current new brand position and to provide a access point for the delivery of new content from Blogs and white papers as well as a portal for information for our current users for gathering Tips and Tricks and access to additional resources to assist them to provide feedback and get support.

Talvoro is Australia's only PPM (Project and Portfolio Management) software provider that caters to the needs of project managers and C-level executives looking for insights into the alignment of resources to business strategy and investment decisions.

As companies gain maturity in PPM there is a need for innovation and management of change beyond just implementation of tools this is why Talvoro has evolved from being a SaaS to becoming a SwS (Software with Service) provider.

Talvoro is recognized as the tool of choice amongst program and project managers that is able to provide the user with an intuitive reliable interface that is capable of evolving and maturing to meet and exceed client requirements.

We are able to provide people at the coalface with tools that enable them to manage resources, scope, time sheeting, issues, changes and risk with excellent reporting functionality.

For C-level executives we are able to provide Business Intelligence (BI) functionality and reporting by integrating the PPM data with other business management systems such as ERP and CRM to provide a insight beyond pure PPM reporting.

We are able to provide Project Management insights from years of experience working with our clients in developing solutions that are inline with the evolution that comes with change.

Please feel free to email me on nigel.brask@talvoro-example.com if you require any further details. A Site map and a wire frame is available.

Competitor sites include

www.plonverk-example.com
www.surmoza-example.com
www.qarnitel-example.com
www.velubra-example.com
Updates

Hi All 

We are getting some great designs coming in and really appreciate all of your efforts.

Some feedback to you all is that we have a preference for cleaner designs that take into account comprehension ability. So reverse type to us looks good but doesnt always get the cut through.

We have to remember that this is a marketing site first and foremost so what we are looking for is the ability to engage with our audience and get them to start to explore. That is upto us to provide great content and what we want from the design is the ability to be be able to engage with our Audience.

For your consideration please review this info from our marketing plan

There are 3 main communication groups inthe sales process.

Users-        These are the peoplewho will be at the coal face inputting the data and using the product on adaily basis. It is key to provide them with an easy to use and functional toolthat is able to provide them with the information they are looking for easily andintuitively. They have the capacity to say yes and can push the sale decisionup the chain. They equally have the power to say No and stop the sales processin its tracks. They will have a opinion who or what they feel is the best ofbreed and will try to influence the process.

Users are split into two groups.

Group1- They will be diploma if not degree qualifiedwill be a mix of Male and female with majority aged 18 to 35 they are at thecareer development stage of their life cycle normally on an income 45k to 70kper annum. We would position these people very strongly in the “What is in itfor me”.

Group2- PM who has used a variety of tools and systemsover the years they will be pre disposed to one or more systems and has morethan likely been exposed to MSP. Usually in the 30 to 50 year old age rangewith extensive on the job experience.

KeyInfluencers- These are the people who while notactually utilizing the software need to receive information in the form ofreports etc from the system. They normally don’t have the capacity to say yesbut they most certainly can say no. They will have come from a PM or IT roleand have a strong understanding of the PM processes. Influencers will be 30 to50 years of age they are at the family development stage with strong demandsfrom work and family predominantly male but not exclusively. They would bedegree qualified and possibly have completed or looking at additional studies. Therewill be an emphasis on getting the job done right. They are very time poor and hardto communicate with and engage. While being time poor they have an affinitywith and understand the greater good.

DecisionMakers- These are our key decision makers whilethey may not have direct input into the system or processes they are at the endof the day the people who approve the expenditure.

There is a huge demand for this person’stime with a multitude of people from internal employees and management,suppliers, customers, the community and potential suppliers. They are oftentravelling and going from one subject matter to another meeting after meeting.They will be at the stage where children are gaining some independents or leftthe home, career is stabilized and a clear path is formed. They are very directand deal in the facts and figures when it comes to decision making, they arenormally highly educated to the MBA or Doctorate level. They will be driven byoutcomes not the process of getting there.

 

A consistent theme across this group isthe following.

Psychographics

·Values time and considers ittheir single most limited resource.

·Excited about accepting andusing innovative ideas and products always wants to be at the fore front.

·Value adding has priority overprice

·Consistent web users: preferinternet over magazines and newspapers

Behavior

·They are leaders in productselection and respond to the opinions of the ‘Industry Experts’ when makingpurchase decisions.

·This group will look to theinternet to acquire the information

·Will make an informed decisionto purchase after due consideration.

·This group can be a powerfulsales force resulting from the referral network they build and use

Hope this helps

Hi All

Sorry for the delay we are in the final stages of decisions, so sorry we have had people away from the office who need to be involved in the process.

We will submit individual questions to those in the running and let all of the people who didnt get through this time as to why shortly.

We would like to thank you all for your efforts and submissions.

Regards

Nigel Brask 

Industry/Entity Type

Business Management

Requirements
Must have
• The scope of the website is to provide a modern functional website that is easy to navigate and provides a range of products and services to meet the needs of our potential clients and current users.

Two potential groups of viewers exist:
1. Potential Clients and users from the Project management community these would be split into 3 distinct groups. ( Please refer to Page 20 Talvoro marketing Plan)
a. Project Managers
b. Project Directors
c. Business Managers
2. Current Talvoro Users

The goal of website is to engage with the project management community reinforcing the Talvoro Brand as Software with Service the key ethos should be around the company being thought leaders and industry experts with a strong commitment to clients and the success of their Portfolio/Program Management Office

Maintaining a modern and user friendly site is of the highest importance in order to hold users attention and guide the viewer to information that will lead to a decision to pursue accreditation and association with the Talvoro Brand

We would like to guide potential clients to want to engage with us in assisting them to understand their current position in the QM5 maturity model and to use us as a source for information and guidance.

Benefits for using the site should include:
• Information from a broad spectrum of Project Management professionals and recognized industry experts.
• Information on the Talvoro Product and Services
• Timely and up to date information that encourages readers to return to the site
• Call to action, and plans for potential users of Talvoro software.
• Demonstrate the benefits of accreditation and Call to action for current users to gain accreditation.
• Call to action for attending monthly webinars
• Ability to review past webinars, whitepapers etc.

```html
<!DOCTYPE html>
<html lang="en">
<head>
<meta charset="utf-8">
<title>Talvoro — Project Management Software</title>
<link rel="stylesheet" href="https://fonts.googleapis.com/css2?family=Inter:wght@300;400;500;600;700&display=swap">
<style>
:root{
  --red:#e0311c;
  --red-dark:#b9220f;
  --ink:#222222;
  --grey:#4a4a4a;
  --muted:#6b6b6b;
  --light:#f2f2f2;
  --dark-band:#272727;
  --green-dark:#127a09;
  --icon-grey:#9a9a9a;
}
*{box-sizing:border-box;margin:0;padding:0}
html,body{width:1172px;height:1200px;overflow:hidden}
body{position:relative;background:var(--light);font-family:"Inter",Arial,sans-serif;color:var(--ink);letter-spacing:-0.01em}
a{color:inherit;text-decoration:none}
.abs{position:absolute}

/* utility navigation */
.utility-bar{left:0;top:0;width:1172px;height:42px;background:#fff;border-bottom:1px solid #e6e6e6}
.utility-nav{left:195px;top:14px;display:flex;font-size:10.5px;color:#444}
.utility-nav a{padding:0 19px;border-left:1px solid #ccc;line-height:14px}
.utility-nav a:first-child{padding-left:0;border-left:none}
.utility-nav a:last-child{padding-right:0}

/* main header */
.brand{left:195px;top:58px;display:flex;align-items:center;gap:7px;font-size:30px;font-weight:400;color:#2a2a2a;letter-spacing:-0.02em}
.brand-dot{width:10px;height:10px;border-radius:50%;background:var(--red)}
.main-nav{left:423px;top:66px;display:flex;font-size:15px;font-weight:500;color:#444;letter-spacing:0.02em}
.main-nav a{padding:0 23px;border-left:1px solid #ccc;line-height:16px}
.main-nav a:first-child{padding-left:0;border-left:none}
.btn-signup{left:748px;top:60px;width:83px;height:29px;background:var(--red);color:#fff;font-size:15px;font-weight:500;display:flex;align-items:center;justify-content:center;border-radius:2px}
.btn-login{left:841px;top:60px;width:136px;height:29px;background:#444;color:#fff;font-size:15px;font-weight:500;display:flex;align-items:center;justify-content:center;border-radius:2px}
.header-rule{left:0;top:104px;width:1172px;border-top:1px dashed #c8c8c8}

/* hero */
.hero{left:0;top:106px;width:1172px;height:291px;background:radial-gradient(ellipse at 45% 40%,#ffffff 45%,#e4e4e4 100%)}
.hero-kicker{left:196px;top:166px;font-size:21px;font-weight:400;color:#444}
.hero-title{left:194px;top:192px;font-size:35px;font-weight:700;color:var(--red);letter-spacing:-0.045em}
.hero-sub{left:194px;top:224px;font-size:34px;font-weight:400;color:#444;letter-spacing:-0.03em}
.btn-tour{left:196px;top:278px;width:200px;height:40px;background:linear-gradient(#27ae17,var(--green-dark));color:#fff;font-size:23px;font-weight:700;display:flex;align-items:center;justify-content:center;border-radius:2px}
.hero-dots{left:196px;top:367px;display:flex;gap:6px}
.hero-dots span{width:11px;height:11px;border-radius:50%;background:#333}
.hero-dots span:first-child{background:var(--red)}
.hero-art{left:600px;top:125px;width:380px;height:280px;border-radius:50%;background:radial-gradient(circle at 55% 45%,#f1f1f1 0%,#e9c29a 28%,#dc8a52 50%,rgba(255,255,255,0) 70%)}
.hero-shadow{left:115px;top:395px;width:940px;height:2px;background:linear-gradient(90deg,transparent,#999,transparent)}

/* features */
.feature{top:437px;width:200px;text-align:center}
.feature-icon{width:84px;height:84px;margin:0 auto;border-radius:50%}
.feature h3{margin-top:12px;font-size:16px;font-weight:600;letter-spacing:-0.03em;color:#222;white-space:nowrap}
.feature h3 em{font-style:normal;color:var(--red)}
.feature p{width:180px;margin:6px auto 0;font-size:12px;line-height:15px;color:#555}
.feature-divider{top:440px;width:1px;height:180px;background:#e2e2e2}

/* pricing */
.pricing{left:0;top:649px;width:1172px;height:240px;background:var(--dark-band)}
.pricing-title{left:195px;top:669px;font-size:20px;font-weight:600;color:#fff;letter-spacing:-0.03em}
.pricing-title em{font-style:normal;color:var(--red)}
.pricing-note{left:376px;top:667px;padding-left:14px;border-left:1px dashed #666;height:28px;line-height:28px;font-size:13px;font-weight:300;color:#bbb}
.plan{top:708px;width:117px;height:157px;text-align:center;border-radius:2px}
.plan h4{margin-top:12px;font-size:15.5px;font-weight:600;letter-spacing:-0.03em}
.plan .plan-rule{margin:7px 6px 0;height:1px}
.plan .price{margin-top:6px;font-size:40px;font-weight:300;letter-spacing:-0.03em;line-height:44px}
.plan .unit{font-size:9.5px;margin-top:3px}
.plan .plan-btn{position:absolute;left:13px;bottom:13px;width:92px;height:31px;display:flex;align-items:center;justify-content:center;font-size:16px;font-weight:600;color:#fff;border-radius:2px}
.plan-light{background:linear-gradient(#ffffff,#dcdcdc);color:#222}
.plan-light .plan-rule{background:#ddd}
.plan-light .price{color:#444}
.plan-light .unit{color:#666}
.plan-light .plan-btn{background:var(--red)}
.plan-red{background:linear-gradient(var(--red),var(--red-dark));color:#fff}
.plan-red .plan-rule{background:rgba(255,255,255,0.25)}
.plan-red .unit{color:#ffd3cc}
.plan-red .plan-btn{background:#2b2b2b}

/* calls to action */
.cta-title{top:913px;font-size:20px;font-weight:600;letter-spacing:-0.03em;color:#222}
.cta-title em{font-style:normal;color:var(--red)}
.cta-text{top:939px;width:250px;font-size:11.8px;line-height:15px;color:#444;letter-spacing:-0.02em}
.cta-btn{top:976px;height:28px;background:var(--red);color:#fff;font-size:14.5px;font-weight:500;display:flex;align-items:center;justify-content:center;border-radius:2px}
.cta-divider{left:452px;top:905px;width:1px;height:100px;background:#ddd}
.review-box{left:726px;top:912px;width:252px;height:93px;background:linear-gradient(100deg,#ffffff 0%,#ececec 60%,#ececec 100%);border:1px solid #ddd;overflow:hidden}
.review-box h4{position:absolute;left:12px;top:14px;font-size:20px;font-weight:600;line-height:20px;letter-spacing:-0.04em;color:#222}
.review-box h4 em{font-style:normal;color:var(--red)}
.review-art{position:absolute;right:0;top:0;width:102px;height:93px;background:linear-gradient(135deg,var(--red),var(--red-dark))}

/* footer */
.footer-rule{left:50px;top:1034px;width:1070px;height:1px;background:linear-gradient(90deg,transparent,#aaa,transparent)}
.footer-brand{left:196px;top:1057px;display:flex;align-items:center;gap:6px;font-size:30px;font-weight:400;color:#8c8c8c;letter-spacing:-0.02em}
.footer-brand .brand-dot{background:#a5a5a5}
.social{left:196px;top:1105px;display:flex;gap:7px}
.social span{width:26px;height:26px;border-radius:50%;background:#555}
.footer-col{top:1058px;display:flex;flex-direction:column;gap:5px;font-size:11px;line-height:13.5px;color:#444}
.newsletter-title{left:726px;top:1052px;font-size:20px;font-weight:600;letter-spacing:-0.03em}
.newsletter-title em{font-style:normal;color:var(--red)}
.newsletter{left:726px;top:1080px;width:252px;height:34px;background:#fff;border:1px solid #ccc;border-radius:2px}
.newsletter .placeholder{position:absolute;left:11px;top:10px;font-size:12px;color:#999}
.newsletter .subscribe{position:absolute;right:4px;top:4px;width:75px;height:24px;background:#222;color:#fff;font-size:12.5px;font-weight:600;display:flex;align-items:center;justify-content:center;border-radius:2px}
.footer-bottom-rule{left:50px;top:1157px;width:1070px;height:1px;background:#dcdcdc}
.copyright{left:195px;top:1170px;font-size:10.5px;color:#555}
</style>
</head>
<body>

<header>
  <div class="abs utility-bar"></div>
  <nav class="abs utility-nav">
    <a href="#">Products &amp; Services</a><a href="#">About Us</a><a href="#">News &amp; Events</a><a href="#">QM5 Self Testing</a><a href="#">Blog</a><a href="#">Accreditation</a><a href="#">Our Uniqueness</a><a href="#">Contact Us</a>
  </nav>
  <div class="abs brand"><span class="brand-dot"></span>talvoro</div>
  <nav class="abs main-nav"><a href="#">TOUR</a><a href="#">FEATURES</a><a href="#">PRICING</a></nav>
  <a class="abs btn-signup" href="#">SIGNUP</a>
  <a class="abs btn-login" href="#">TALVORO LOGIN</a>
  <div class="abs header-rule"></div>
</header>

<section>
  <div class="abs hero"></div>
  <div class="abs hero-art" role="img" aria-label="Illustration of orange and white cubes breaking apart from a puzzle cube"></div>
  <p class="abs hero-kicker">SIMPLE, EASY TO USE</p>
  <h1 class="abs hero-title">PROJECT MANAGEMENT</h1>
  <p class="abs hero-sub">SOFTWARE</p>
  <a class="abs btn-tour" href="#">TAKE A TOUR</a>
  <div class="abs hero-dots"><span></span><span></span><span></span><span></span><span></span></div>
  <div class="abs hero-shadow"></div>
</section>

<section>
  <div class="abs feature" style="left:187px">
    <div class="feature-icon" role="img" aria-label="Gear badge icon for project management" style="background:radial-gradient(circle,#2a2a2a 55%,var(--icon-grey) 58%)"></div>
    <h3>Project <em>Management</em></h3>
    <p>Simple, easy to use project management software. Plan, Track and Improve your projects. Reduce costs and increase efficiency.</p>
  </div>
  <div class="abs feature-divider" style="left:386px"></div>
  <div class="abs feature" style="left:387px">
    <div class="feature-icon" role="img" aria-label="Gear badge icon for timesheets" style="background:radial-gradient(circle,#f0701e 55%,var(--icon-grey) 58%)"></div>
    <h3>Time<em>sheets</em></h3>
    <p>Powerful hosted project time and status collection. Track expenses and time. Have an audit trail on your time billing. Timesheet software</p>
  </div>
  <div class="abs feature-divider" style="left:586px"></div>
  <div class="abs feature" style="left:587px">
    <div class="feature-icon" role="img" aria-label="Gear badge icon for resource management" style="background:radial-gradient(circle,#d8331d 55%,var(--icon-grey) 58%)"></div>
    <h3>Resource <em>Management</em></h3>
    <p>Plan, manage and control work for your whole organisation or a single project. Resource management</p>
  </div>
  <div class="abs feature-divider" style="left:786px"></div>
  <div class="abs feature" style="left:787px">
    <div class="feature-icon" role="img" aria-label="Gear badge icon for issues and risks" style="background:radial-gradient(circle,#4a2b8c 55%,var(--icon-grey) 58%)"></div>
    <h3>Issues, Risks <em>and change</em></h3>
    <p>Track and report on issues, risk and change. One click reports. issue management</p>
  </div>
</section>

<section>
  <div class="abs pricing"></div>
  <h2 class="abs pricing-title">User <em>Pricing Plans</em></h2>
  <p class="abs pricing-note">Web Exclusive Prices for Lite Desktop Version</p>

  <div class="abs plan plan-light" style="left:195px"><h4>Single User</h4><div class="plan-rule"></div><div class="price">$65</div><div class="unit">per month</div><a class="plan-btn" href="#">Sign Up</a></div>
  <div class="abs plan plan-red" style="left:328px"><h4>5 User Pack</h4><div class="plan-rule"></div><div class="price">$65</div><div class="unit">per user per month</div><a class="plan-btn" href="#">Sign Up</a></div>
  <div class="abs plan plan-light" style="left:461px"><h4>10 User Pack</h4><div class="plan-rule"></div><div class="price">$59</div><div class="unit">per user per month</div><a class="plan-btn" href="#">Sign Up</a></div>
  <div class="abs plan plan-red" style="left:594px"><h4>15 User Pack</h4><div class="plan-rule"></div><div class="price">$55</div><div class="unit">per user per month</div><a class="plan-btn" href="#">Sign Up</a></div>
  <div class="abs plan plan-light" style="left:726px"><h4>20 User Pack</h4><div class="plan-rule"></div><div class="price">$49</div><div class="unit">per user per month</div><a class="plan-btn" href="#">Sign Up</a></div>
  <div class="abs plan plan-red" style="left:859px"><h4>20+ Users</h4><a class="plan-btn" href="#" style="width:94px;left:12px">Contact Us</a></div>
</section>

<section>
  <h3 class="abs cta-title" style="left:196px">See it in <em>Action</em></h3>
  <p class="abs cta-text" style="left:196px;width:250px">Login and see the power of Talvoro for yourself in our demo enviorment.</p>
  <a class="abs cta-btn" href="#" style="left:196px;width:117px">LOGIN HERE</a>
  <div class="abs cta-divider"></div>
  <h3 class="abs cta-title" style="left:466px">Join this month’s <em>Webinar</em></h3>
  <p class="abs cta-text" style="left:466px;width:245px">Duis autem vel eum iriure dolor in hendrerit in vulputate velit esse.</p>
  <a class="abs cta-btn" href="#" style="left:466px;width:146px">REGISTER HERE</a>
  <div class="abs review-box">
    <h4>Review Past<br><em>Webinars,<br>Whitepapers</em></h4>
    <div class="review-art" role="img" aria-label="Illustration of stacked papers with a green pencil"></div>
  </div>
</section>

<footer>
  <div class="abs footer-rule"></div>
  <div class="abs footer-brand"><span class="brand-dot"></span>talvoro</div>
  <div class="abs social" aria-label="Social links"><span></span><span></span><span></span></div>
  <nav class="abs footer-col" style="left:367px"><a href="#">Home</a><a href="#">FAQ</a><a href="#">Support &amp; Training</a><a href="#">Contact Us</a></nav>
  <nav class="abs footer-col" style="left:503px"><a href="#">Tour</a><a href="#">Features</a><a href="#">Pricing</a><a href="#">Sign Up</a></nav>
  <nav class="abs footer-col" style="left:598px"><a href="#">Careers</a><a href="#">Privacy Policy</a><a href="#">Terms of Sale</a><a href="#">Sitemap</a></nav>
  <h3 class="abs newsletter-title">Subscribe to <em>Newsletter</em></h3>
  <div class="abs newsletter"><span class="placeholder">Email Address</span><span class="subscribe">Subscribe</span></div>
  <div class="abs footer-bottom-rule"></div>
  <p class="abs copyright">© 2003 - 2012 talvoro pty. ltd. All Rights Reserved</p>
</footer>

</body>
</html>
```